Business Card Design for Occupational Medicine Start Up Company

We need to design a professional business card. We are a healthcare company providing occupational medicine services to blue collar industries. We are professional, efficient and high quality service providers.

Target Market(s)

Blue Collar Industry: Shipbuilding, Ports, Trucking Companies; The Executives and Safety Officers for these companies

Industry/Entity Type

Healthcare

Contact Information for Business Card

Logo, Name, Title, Email, Phone

Other font styles liked:
• Please match our Brand Guide

Requirements
Must have
• Our Company Colors and Logo

```html
<!DOCTYPE html>
<html lang="en">
<head>
<meta charset="utf-8">
<title>CrewSafe Clinics – Business Card</title>
<link rel="stylesheet" href="https://fonts.googleapis.com/css2?family=Montserrat:wght@700&family=Arimo:wght@400&display=swap">
<style>
  :root {
    --backdrop: #dcdcdc;
    --backdrop-edge: #b9b9b9;
    --navy: #1b2a86;
    --navy-text: #25358c;
    --ink: #111111;
    --white: #ffffff;
    --gold: #f4b740;
    --sky: #45aee8;
    --rule: #dedede;
    --muted: #444444;
  }
  * { margin: 0; padding: 0; box-sizing: border-box; }
  html, body {
    width: 1200px;
    height: 900px;
    overflow: hidden;
  }
  body {
    position: relative;
    background: radial-gradient(ellipse at 55% 45%, var(--backdrop) 0%, var(--backdrop-edge) 100%);
    font-family: "Arimo", Arial, sans-serif;
  }
  .card {
    position: absolute;
    width: 560px;
    height: 320px;
    box-shadow: 0 6px 18px rgba(0, 0, 0, 0.28);
  }

  /* Front side */
  .card-front {
    left: 220px;
    top: 90px;
    background: linear-gradient(135deg, #1e2f8f 0%, var(--navy) 60%, #17247a 100%);
    display: flex;
    align-items: center;
    justify-content: center;
  }
  .brand {
    display: flex;
    align-items: center;
    gap: 14px;
  }
  .brand-dot {
    width: 34px;
    height: 34px;
    border-radius: 50%;
    background: var(--gold);
    flex-shrink: 0;
  }
  .brand-name {
    font-family: "Montserrat", Arial, sans-serif;
    font-weight: 700;
    letter-spacing: 0.5px;
  }
  .card-front .brand-name {
    color: var(--white);
    font-size: 30px;
  }

  /* Back side */
  .card-back {
    left: 420px;
    top: 480px;
    background: var(--white);
  }
  .card-back .brand {
    position: absolute;
    left: 34px;
    top: 36px;
    gap: 10px;
  }
  .card-back .brand-dot {
    width: 26px;
    height: 26px;
  }
  .card-back .brand-name {
    color: var(--navy);
    font-size: 20px;
  }
  .holder {
    position: absolute;
    right: 42px;
    top: 150px;
    text-align: right;
  }
  .holder-name {
    font-size: 28px;
    color: var(--navy-text);
    line-height: 1;
  }
  .holder-title {
    font-size: 11px;
    color: var(--ink);
    margin-top: 3px;
  }
  .divider {
    position: absolute;
    left: 96px;
    right: 0;
    top: 228px;
    height: 1px;
    background: var(--rule);
  }
  .contact {
    position: absolute;
    left: 100px;
    top: 244px;
    list-style: none;
  }
  .contact li {
    display: flex;
    align-items: center;
    gap: 12px;
    font-size: 15px;
    color: var(--ink);
    line-height: 24px;
  }
  .contact svg {
    width: 14px;
    height: 14px;
    fill: var(--navy);
  }
</style>
</head>
<body>

  <section class="card card-front" aria-label="Business card front">
    <div class="brand">
      <span class="brand-dot"></span>
      <span class="brand-name">CrewSafe Clinics</span>
    </div>
  </section>

  <section class="card card-back" aria-label="Business card back">
    <div class="brand">
      <span class="brand-dot"></span>
      <span class="brand-name">CrewSafe Clinics</span>
    </div>

    <div class="holder">
      <p class="holder-name">Marisol</p>
      <p class="holder-title">Manager</p>
    </div>

    <div class="divider"></div>

    <ul class="contact">
      <li>
        <svg viewBox="0 0 24 24" aria-hidden="true"><path d="M6.6 10.8c1.4 2.8 3.8 5.1 6.6 6.6l2.2-2.2c.3-.3.7-.4 1-.2 1.1.4 2.3.6 3.6.6.6 0 1 .4 1 1V20c0 .6-.4 1-1 1C10.6 21 3 13.4 3 4c0-.6.4-1 1-1h3.5c.6 0 1 .4 1 1 0 1.3.2 2.5.6 3.6.1.3 0 .7-.2 1z"/></svg>
        <span>555 210 4837</span>
      </li>
      <li>
        <svg viewBox="0 0 24 24" aria-hidden="true"><path d="M2 5h20v14H2z M4 7v.5l8 5.5 8-5.5V7l-8 5.5z" fill-rule="evenodd"/></svg>
        <span>info@crewsafehealth.com</span>
      </li>
    </ul>
  </section>

</body>
</html>
```